Corporate Financing/Banking Website Design

I need a website for a corporate financing website.

The company helps other companies raise money for financing.

Content for the website can be found here: https://www.plumsite.ca/northwavecapital/

Each section from the content in the main page above should have a corresponding image associated with each "Section"

1. Financing solutions that will be provided by Corven Ridge Finance will include:

2. The financing solutions mentioned above will assist businesses to:

3. The industry sectors focussed on are, but not limited to:

We need to make sure that the website has clear buttons for the visitor to "Apply Now" and "Book an Appointment" to apply for financing options.

We need the following pages designed
Home
About Us
Financing Solutions
Contact Us.

For the Logo:

The company name is Corven Ridge Finance. Something that emphasizes direction and progress and is related to Corporate finance

Something professional that conveys confidence

Target Market(s)

Corporation and large business

Logo Text

Corven Ridge Finance

Number of Pages Required

4 page

Colors
0393ce

Requirements
Must have
• Use the color: #OA64BC

Please ensure 'Apply Now' & 'Book an Appointment' buttons are very clear and placed appropriately on the webpage.

In the Footer I would like 'T&C's' and 'Privacy Policy' links

Social Media icon links will be 'LinkedIn / Facebook/ Twitter and we should keep these in Footer and Contacts page section.
Should not have
• - Do not include a search field

```html
<!DOCTYPE html>
<html lang="en">
<head>
<meta charset="utf-8">
<title>Corven Ridge Finance</title>
<link rel="stylesheet" href="https://fonts.googleapis.com/css2?family=Lora:wght@600;700&family=Lato:wght@400;700&display=swap">
<style>
:root{
  --bg:#f0f9fe;
  --primary:#0a6fc0;
  --accent:#1f86cc;
  --ink:#111111;
  --muted:#555a60;
  --line:#d9e4ec;
  --card:#ffffff;
  --footer:#1176c6;
}
*{margin:0;padding:0;box-sizing:border-box}
html,body{width:1200px;height:3266px;overflow:hidden}
body{background:var(--bg);font-family:'Lato',sans-serif;color:var(--ink);position:relative}
.abs{position:absolute}
.serif{font-family:'Lora',serif;font-weight:700}
.btn{position:absolute;background:var(--primary);color:#fff;font-size:13px;font-weight:700;display:flex;align-items:center;justify-content:center;border-radius:3px}
.topbar{top:0;left:0;width:1200px;height:48px}
.topbar .social{position:absolute;top:13px;left:98px;display:flex;gap:16px}
.dot{width:9px;height:9px;border-radius:50%;background:#707a84;display:block}
.topbar .info{position:absolute;top:12px;font-size:13px;color:#6b737b}
.rule{position:absolute;top:38px;left:98px;width:1004px;height:1px;background:var(--line)}
.brand{top:68px;left:98px;display:flex;align-items:center;gap:10px}
.brand .mark{width:34px;height:34px;background:var(--primary);display:block}
.brand span{font-family:'Lora',serif;font-weight:700;font-size:22px;color:var(--primary)}
.nav{top:80px;left:472px;display:flex;gap:0;font-size:14px;color:#333}
.nav a{position:absolute;white-space:nowrap;color:#333;text-decoration:none}
.nav a.active{color:var(--primary)}
.hero-title{top:252px;left:98px;font-size:54px;line-height:48px}
.hero-text{top:366px;left:99px;width:450px;font-size:18px;line-height:25px;color:#555}
.hero-art{top:120px;left:533px;width:533px;height:490px;border-radius:40%;background:radial-gradient(circle at 55% 55%,#d6ecf8 0%,#e9f5fc 45%,rgba(240,249,254,0) 70%)}
.welcome{top:668px;left:0;width:1200px;text-align:center;font-size:50px;line-height:52px}
.welcome .blue{color:var(--accent)}
.welcome-text{top:790px;left:165px;width:870px;text-align:center;font-size:13px;line-height:22.5px;color:#555}
.card{position:absolute;width:213px;height:224px;background:var(--card);box-shadow:6px 10px 22px rgba(20,60,100,.12);display:flex;flex-direction:column;align-items:center;justify-content:center;gap:14px;text-align:center;font-size:18px;line-height:25px;color:#222}
.card svg{width:60px;height:60px}
.label-blue{top:1094px;left:336px;font-size:18px;line-height:27px;color:var(--accent)}
.sol-title{top:1094px;left:606px;font-size:32px;line-height:40px;width:500px}
.sol-text{top:1230px;left:606px;width:490px;font-size:13px;line-height:27px;color:#555}
.sec-title{left:0;width:1200px;text-align:center}
.benefit{position:absolute;width:300px;text-align:center;font-size:19px;line-height:26px;color:#222}
.benefit .ring{width:81px;height:81px;border-radius:50%;background:#fff;box-shadow:5px 8px 16px rgba(20,60,100,.14);margin:0 auto 22px;display:flex;align-items:center;justify-content:center}
.benefit svg{width:46px;height:46px}
.sector{position:absolute;top:2276px;width:251px;height:293px;display:flex;align-items:flex-end;padding:0 0 18px 19px;color:#fff;font-family:'Lora',serif;font-weight:700;font-size:23px}
.next{top:2399px;left:1102px;width:48px;height:48px;border-radius:50%;background:#fff;box-shadow:0 4px 14px rgba(20,60,100,.15);display:flex;align-items:center;justify-content:center}
.cta{top:2672px;left:0;width:1200px;text-align:center;font-size:32px;line-height:38px}
.footer{top:2909px;left:0;width:1200px;height:357px;background:var(--footer);color:#fff}
.footer h4{position:absolute;top:60px;font-family:'Lora',serif;font-weight:700;font-size:23px}
.footer ul{position:absolute;top:118px;list-style:none;font-size:13px;line-height:22.5px}
.footer .fsocial{position:absolute;top:126px;left:662px;display:flex;gap:21px}
.footer .fsocial i{width:8px;height:8px;border-radius:50%;background:#fff;display:block}
.copy{position:absolute;top:330px;left:0;width:1200px;text-align:center;font-size:12px}
.code{position:absolute;top:332px;left:1144px;font-size:10px;opacity:.8}
</style>
</head>
<body>

<header class="abs topbar">
  <div class="social"><i class="dot"></i><i class="dot"></i><i class="dot"></i></div>
  <div class="info" style="left:455px">
    <svg width="11" height="11" viewBox="0 0 24 24" style="vertical-align:-1px"><path d="M6 2l4 4-2 3c1 3 4 6 7 7l3-2 4 4-3 4C10 22 2 14 2 5z" fill="#707a84"/></svg>
    &nbsp;+ 888 888 8888</div>
  <div class="info" style="left:641px">
    <svg width="12" height="10" viewBox="0 0 24 18" style="vertical-align:-1px"><rect width="24" height="18" rx="2" fill="#707a84"/><path d="M1 2l11 8 11-8" stroke="#fff" stroke-width="2" fill="none"/></svg>
    &nbsp;info@corvenridgefinance.com</div>
  <div class="btn" style="left:913px;top:3px;width:189px;height:31px">Book an Appointment</div>
</header>
<div class="rule"></div>

<div class="abs brand"><i class="mark"></i><span>CORVEN RIDGE FINANCE</span></div>

<nav class="abs nav">
  <a class="active" style="left:0">Home</a>
  <a style="left:91px">About Us</a>
  <a style="left:206px">Financing Solutions</a>
  <a style="left:386px">Contact Us</a>
</nav>
<div class="btn" style="left:981px;top:74px;width:121px;height:31px">Apply Now</div>

<h1 class="abs serif hero-title">Corven Ridge<br>Finance</h1>
<p class="abs hero-text">Lorem ipsum dolor sit amet, consectetur adipiscing elit, sed do eiusmod tempor incididunt</p>
<div class="btn" style="left:100px;top:442px;width:122px;height:30px">Apply Now</div>
<div class="abs hero-art" role="img" aria-label="Isometric illustration of rising bar columns, an upward arrow, coins, banknotes, a bank card, an hourglass and a person working on a laptop"></div>

<h2 class="abs serif welcome">Welcome To<br><span class="blue">Corven Ridge Finance</span></h2>
<p class="abs welcome-text">Corven Ridge Finance was created by its founder and CEO, Marek Halloran, for the purpose of meeting the continued growing requirements of businesses for working capital solutions in the frame of operational efficiency, business growth and credit risk mitigation needs.Corven Ridge Finance brings global, regional and local experience in trade finance, supply chain finance and commodity finance to the marketplace and will be best placed to structure, tailor and provide a financing solution for your business.</p>

<div class="card" style="left:102px;top:990px">
  <svg viewBox="0 0 60 60" fill="none" stroke="var(--primary)" stroke-width="2"><rect x="12" y="16" width="36" height="22" rx="2"/><circle cx="30" cy="27" r="6"/><path d="M6 40c8 0 12 6 22 6h14l10-8"/></svg>
  <div>Receivables<br>Financing</div>
</div>
<div class="card" style="left:334px;top:1163px">
  <svg viewBox="0 0 60 60" fill="none" stroke="var(--primary)" stroke-width="2"><rect x="18" y="6" width="24" height="34"/><path d="M22 24h16M22 30h16M22 35h10"/><rect x="8" y="22" width="44" height="28"/><path d="M30 12v8"/></svg>
  <div>Receivables<br>Financing</div>
</div>
<div class="card" style="left:102px;top:1234px">
  <svg viewBox="0 0 60 60" fill="none" stroke="var(--primary)" stroke-width="2"><rect x="22" y="10" width="30" height="32" rx="2"/><path d="M30 32l14-14"/><circle cx="32" cy="20" r="3"/><circle cx="42" cy="31" r="3"/><ellipse cx="16" cy="36" rx="9" ry="3"/><path d="M7 36v14c0 2 18 2 18 0V36M7 41c0 2 18 2 18 0M7 46c0 2 18 2 18 0"/></svg>
  <div>Factoring</div>
</div>

<p class="abs label-blue">Receivables Finance,<br>which includes</p>
<h2 class="abs serif sol-title">Financing solutions that will be provided by Corven Ridge Finance will include</h2>
<p class="abs sol-text">with structured optionsof; disclosed, confidential, single debtor, single invoice, multi debtor or total pool purchase financing available.</p>

<h2 class="abs serif sec-title" style="top:1566px;font-size:52px;line-height:60px">The financing solutions</h2>
<p class="abs serif sec-title" style="top:1622px;font-size:32px;color:var(--accent)">mentioned above will assist businesses to</p>

<div class="benefit" style="left:85px;top:1689px"><div class="ring"><svg viewBox="0 0 46 46" fill="none" stroke="var(--primary)" stroke-width="2"><rect x="5" y="12" width="36" height="22" rx="2"/><circle cx="23" cy="23" r="5"/><circle cx="13" cy="23" r="2"/><circle cx="33" cy="23" r="2"/></svg></div>Monetise Its Receivables<br>To Accelerate Its Cash Cycle</div>
<div class="benefit" style="left:467px;top:1689px"><div class="ring"><svg viewBox="0 0 46 46" fill="none" stroke="var(--primary)" stroke-width="2"><path d="M6 40h34M10 40V28M17 40V24M24 40V30M31 40V22M38 40V26"/><path d="M6 26l10-10 8 6 14-14"/></svg></div>Mitigate Debtor<br>Credit Risk</div>
<div class="benefit" style="left:847px;top:1689px"><div class="ring"><svg viewBox="0 0 46 46" fill="none" stroke="var(--primary)" stroke-width="2"><path d="M6 20l17-10 17 10z"/><path d="M10 22v14M18 22v14M28 22v14M36 22v14M5 38h36"/></svg></div>Minimise Payment<br>Risks</div>
<div class="benefit" style="left:272px;top:1886px"><div class="ring"><svg viewBox="0 0 46 46" fill="none" stroke="var(--primary)" stroke-width="2"><rect x="10" y="6" width="26" height="34"/><path d="M15 14h16M15 20h16M15 26h10"/><circle cx="31" cy="32" r="4"/></svg></div>Optimise Credit Limits So<br>As To Boost Sales Growth</div>
<div class="benefit" style="left:654px;top:1886px"><div class="ring"><svg viewBox="0 0 46 46" fill="none" stroke="var(--primary)" stroke-width="2"><path d="M14 12h10l-3 6c8 4 9 18-2 20-10-2-10-16-2-20z"/><circle cx="33" cy="16" r="8"/><path d="M26 30h14v10H26z"/></svg></div>Use Its Working Capital To<br>Fund Its Business</div>

<h2 class="abs serif sec-title" style="top:2134px;font-size:55px;line-height:58px">The industry sectors focussed<br>on are, but not limited to</h2>

<div class="sector" style="left:0;background:linear-gradient(180deg,#7aa9cf 0%,#8c9a7d 55%,#4a5042 100%)" role="img" aria-label="Aerial photo of a highway interchange and city">Infrastructure</div>
<div class="sector" style="left:265px;background:linear-gradient(180deg,#d9dde3 0%,#9aa2ad 55%,#3e4650 100%)" role="img" aria-label="Photo of hands writing next to a laptop keyboard">Resources</div>
<div class="sector" style="left:531px;background:linear-gradient(180deg,#8b929a 0%,#a6aa6a 55%,#3a3f36 100%)" role="img" aria-label="Photo of two engineers in hard hats reviewing a tablet in a factory">Industrial</div>
<div class="sector" style="left:798px;background:linear-gradient(180deg,#4d6a8a 0%,#c7866b 50%,#3d3a40 100%)" role="img" aria-label="Photo of a telecommunications tower against a sunset sky">Telecomm</div>
<div class="abs next"><svg width="14" height="14" viewBox="0 0 14 14"><path d="M5 2l5 5-5 5" stroke="#333" stroke-width="1.6" fill="none"/></svg></div>

<h2 class="abs serif cta">We look forward to providing financing solutions<br>that will answer your working capital needs.</h2>
<div class="btn" style="left:505px;top:2770px;width:189px;height:31px">Book an Appointment</div>

<footer class="abs footer">
  <h4 style="left:98px">Links</h4>
  <ul style="left:98px"><li>Home</li><li>About Us</li><li>Financing Solutions</li><li>Contact Us</li></ul>
  <h4 style="left:378px">Others</h4>
  <ul style="left:380px"><li>Terms &amp; Conditions</li><li>Privacy Policy</li></ul>
  <h4 style="left:660px">Follow Us</h4>
  <div class="fsocial"><i></i><i></i><i></i></div>
  <h4 style="left:910px">Contact Us</h4>
  <ul style="left:911px"><li>Commercial Suite 4, 210-214</li><li>Harbour Crest Road,</li><li>NSW 2031,Australia</li><li>info@corvenridgefinance.com</li><li>+8 888 888 888</li></ul>
  <p class="copy">Copyrights © 2021, The Company Name. All rights reserved.</p>
  <span class="code">C28</span>
</footer>

</body>
</html>
```